Exclusive British Dental Clinic Needs Modern Brochure to Attract New Patients

We are looking to create a smart, sophisticated brochure that gives the public and future potential clients a concise overview of what we offer and why the quality and care on offer is a step above the rest. We are based in the United Kingdom where the Civic Wellness Bureau provide dental care free or at low cost. We are NOT an CWB provider. We are a wholly private dental clinic so all of our patients are paying full-price premium prices directly out of pocket. The work we do is exceptional so all of our patients can be assured that anything we do is done to the highest and best quality possible.
We offer high quality dental treatment using the best and latest techniques, materials and an award winning dental laboratory. All treatments are undertaken using high quality magnification to ensure the best possible result. We have over 30 years’ experience in general dentistry with fully trained staff. In quality comfortable surroundings, we are a caring practice with excellent patient care. We allow more time with our patients and we understand and care for nervous patients.
We also offer facial fillers, wrinkle reducers and teeth whitening in order to help our patients achieve their best look.

We have attached our logo and logo icons to this brief.
We also have attached some information in our Brochure Details document. This just highlights what we would like to see and more information about us.
We are really up to suggestion with design and wording because we want this brochure to be attractive and appealing to the public.
Feel free to edit as you see fit to help us attain our goals :)

Reason: Hello We are very excited about the work we have received thus far...our Practice Manager is away for the next week and we wanted to make sure we are all on board for the discussions and decisions we make moving forward. Thank you for taking the time to help us create our voice! --- Larkfield Atelier Dental Clinic

```html
<!DOCTYPE html>
<html lang="en">
<head>
<meta charset="utf-8">
<title>Larkfield Atelier Dental Clinic – Brochure Outside</title>
<link rel="stylesheet" href="https://fonts.googleapis.com/css2?family=Mulish:wght@300;400;600;700&display=swap">
<style>
  :root {
    --stage: #3a3a3b;
    --paper: #ffffff;
    --slate-top: #5f7689;
    --slate-bottom: #3f5466;
    --accent: #7fa3d3;
    --accent-dark: #6b90c4;
    --navy: #253c68;
    --ink: #4a4a4a;
    --label: #c9c9c9;
    --rule: #a9c0e0;
  }
  * { box-sizing: border-box; margin: 0; padding: 0; }
  html, body { width: 1200px; height: 900px; overflow: hidden; }
  body { background: var(--stage); font-family: "Mulish", sans-serif; position: relative; }

  .brochure { position: absolute; left: 44px; top: 57px; width: 1113px; height: 786px; background: var(--paper); display: flex; }
  .panel { position: relative; height: 100%; }

  /* Left panel */
  .panel--intro { width: 371px; background: linear-gradient(180deg, var(--slate-top), var(--slate-bottom)); color: #fff; overflow: hidden; }
  .intro__title { position: absolute; left: 30px; top: 60px; font-weight: 300; font-size: 23px; letter-spacing: 0.3px; }
  .intro__body { position: absolute; left: 30px; top: 110px; width: 278px; font-size: 12.2px; line-height: 19.5px; font-weight: 400; }
  .intro__body p + p { margin-top: 19.5px; }
  .intro__photo { position: absolute; left: 85px; top: 410px; width: 286px; height: 376px;
    background: linear-gradient(180deg, #a9c2dc 0%, #8fa9c6 60%, #44566b 100%); border-radius: 120px 120px 0 0; opacity: .85; }

  /* Middle panel */
  .panel--contact { width: 370px; border-right: 1px solid #e6e6e6; }
  .web { position: absolute; top: 344px; left: 0; right: 0; text-align: center; color: var(--accent); font-size: 15px; letter-spacing: 2.6px; }
  .web__icon { display: inline-block; width: 15px; height: 15px; border: 1px solid var(--accent); border-radius: 50%; vertical-align: -2px; margin-right: 6px; }
  .contact { position: absolute; top: 642px; left: 0; right: 0; text-align: center; color: var(--ink); font-size: 10.5px; line-height: 14px; }
  .contact__name { color: var(--accent-dark); font-weight: 700; font-size: 12px; letter-spacing: .3px; }
  .contact__line { position: absolute; top: 43px; left: 0; right: 0; }
  .contact__line b { color: var(--accent-dark); font-weight: 700; margin-right: 4px; }
  .contact__line span + b { margin-left: 12px; }
  .social { position: absolute; left: 30px; right: 30px; top: 709px; border-top: 2px dotted var(--rule); border-bottom: 2px dotted var(--rule); padding: 6px 0 4px; text-align: center; }
  .social__item { color: var(--accent); font-size: 14px; letter-spacing: .8px; line-height: 22px; }
  .social__item::before { content: ""; display: inline-block; width: 14px; height: 14px; border: 1px solid var(--accent); border-radius: 50%; vertical-align: -2px; margin-right: 6px; }

  /* Right panel */
  .panel--cover { width: 372px; }
  .cover__tagline { position: absolute; top: 116px; left: 0; right: 0; text-align: center; color: #6a6a6a; font-weight: 300; font-size: 23px; letter-spacing: 1px; }
  .cover__tagline .smile { color: var(--accent); font-size: 34px; vertical-align: -3px; margin-left: 10px; }
  .cover__photo { position: absolute; left: 6px; right: 0; top: 205px; height: 465px; background: linear-gradient(135deg, #f4f1ee 0%, #c79a7c 45%, #6b4330 75%, #e9e4df 100%); }
  .brand { position: absolute; top: 700px; left: 60px; display: flex; align-items: center; gap: 12px; }
  .brand__mark { width: 40px; height: 40px; border: 2px solid var(--accent-dark); border-radius: 50%; }
  .brand__name { color: var(--navy); font-size: 19px; letter-spacing: .8px; line-height: 20px; font-weight: 400; }
  .brand__name small { display: block; font-size: 10px; letter-spacing: 2.6px; }

  .sheet-label { position: absolute; right: 45px; top: 864px; color: var(--label); font-size: 15px; }
</style>
</head>
<body>
  <div class="brochure">
    <section class="panel panel--intro">
      <h2 class="intro__title">Because&nbsp; you deserve it.</h2>
      <div class="intro__body">
        <p>Having an attractive smile can greatly increase your self-confidence and the positive impression you make on others.</p>
        <p>Of course, not everyone is naturally blessed with a beautiful smile. Fortunately, Larkfield Atelier Dental Clinic is here to help and support you. Modern cosmetic dentistry can transform your smile and the way you feel about yourself. In addition, undergoing such treatment can be a good way to improve your health and general well-being.</p>
        <p>So if you are unhappy with your smile in any way, come and see us at Larkfield Atelier Dental Clinic Ashbury.</p>
      </div>
      <div class="intro__photo" role="img" aria-label="Photo of a smiling couple in light blue shirts and jeans"></div>
    </section>

    <section class="panel panel--contact">
      <p class="web"><span class="web__icon"></span>www.larkfieldatelier.com</p>
      <div class="contact">
        <p class="contact__name">LARKFIELD ATELIER DENTAL CLINIC</p>
        <p>14 Larkfield Row, Ashbury</p>
        <p>Westshire, AB12 3CD</p>
        <p class="contact__line"><b>T</b><span>01632 960 418</span><b>E</b><span>enquiries@larkfieldatelier.com</span></p>
      </div>
      <div class="social">
        <p class="social__item">friendbook.net/LarkfieldAtelier</p>
        <p class="social__item">chirper.net/Larkfield_Dental</p>
      </div>
    </section>

    <section class="panel panel--cover">
      <h1 class="cover__tagline">Freedom to <span class="smile">:)</span></h1>
      <div class="cover__photo" role="img" aria-label="Photo of a smiling woman with long brown hair"></div>
      <div class="brand">
        <span class="brand__mark"></span>
        <p class="brand__name">LARKFIELD ATELIER<small>DENTAL CLINIC</small></p>
      </div>
    </section>
  </div>
  <p class="sheet-label">Outside</p>
</body>
</html>
```